International PR and marketing agency needs website design

We need a branding website, for a company based in the US (Washington DC). We are a communication (PR, marketing, social media) agency. We already have the copy, and we have some example websites (some major agencies), that we like.
For example:
https://pellowtrask.example/
https://durnevaleglobal.example/
https://varnok.example/
https://qmf-reach.example/
https://www.thornbury.example/
The website must be a multi-language site, we will add the new languages step-by-step.
We would like to upload content continuously.
The website has to have sub-pages (segments), and news part.
Target Market(s)
Global
Industry/Entity Type
Public relations, Communications, Marketing, Social Media
Number of Pages Required
5+ page
Font styles to use
Other font styles liked:
- Well readable, modern style.
Look and feel

```html
<!DOCTYPE html>
<html lang="en">
<head>
<meta charset="utf-8">
<title>Lumenway PR</title>
<link href="https://fonts.googleapis.com/css2?family=Figtree:wght@400;500;600;700;800&display=swap" rel="stylesheet">
<style>
:root{
  --pink:#e0479a;
  --pink-deep:#c72a80;
  --blush:#fce9f2;
  --blush-soft:#fdf2f7;
  --ink:#111;
  --grey:#555;
  --white:#fff;
  --night:#050505;
}
*{box-sizing:border-box;margin:0;padding:0}
html,body{width:1200px;height:4060px;overflow:hidden}
body{position:relative;background:var(--white);font-family:"Figtree",sans-serif;color:var(--ink)}
.abs{position:absolute}
.band{position:absolute;left:0;width:1200px;overflow:hidden}
.btn{position:absolute;background:var(--pink);color:var(--white);border-radius:20px;font-weight:600;font-size:17px;display:flex;align-items:center;justify-content:center;letter-spacing:.3px}
.photo{position:absolute}
h1,h2{font-weight:800;line-height:1.13}
.kicker{font-size:26px;font-weight:500;display:flex;align-items:center;gap:12px}
.copy{font-size:16.5px;line-height:1.1;color:#333;white-space:nowrap}

/* header + hero */
.hero{top:0;height:577px;background:var(--blush)}
.brand{position:absolute;display:flex;align-items:center;gap:7px;font-weight:800;color:var(--pink-deep);white-space:nowrap}
.brand .dot{border-radius:50%;background:var(--pink-deep);flex:none}
.brand-head{left:91px;top:24px;font-size:18px}
.brand-head .dot{width:30px;height:30px}
.nav a{position:absolute;top:30px;font-size:16px;font-weight:500;color:#333;text-decoration:none}
.nav a.active{color:var(--pink)}
.contact-btn{position:absolute;left:941px;top:20px;width:168px;height:38px;border-radius:20px;background:var(--white);color:var(--pink);font-size:17px;display:flex;align-items:center;justify-content:center}

/* expertise */
.expertise{top:1333px;height:607px;background:var(--blush)}
.card{position:absolute;width:270px;height:210px;background:var(--white);border-radius:0 0 34px 0;padding:26px 36px}
.card svg{width:52px;height:52px;stroke:#333;fill:none;stroke-width:1.6}
.card h3{font-size:21px;font-weight:500;margin-top:14px}
.card p{font-size:12.5px;color:#555;line-height:1.1;margin-top:8px}
.card .more{font-size:12px;font-weight:700;margin-top:14px}

/* news */
.news-card{position:absolute;top:2156px;width:257px;height:277px;border-radius:0 0 0 34px;overflow:hidden}
.news-card .shade{position:absolute;inset:0;background:linear-gradient(180deg,rgba(0,0,0,0) 40%,rgba(0,0,0,.7))}
.news-card .txt{position:absolute;left:30px;top:190px;width:215px;color:var(--white)}
.news-card b{font-size:16px}
.news-card p{font-size:12.5px;line-height:1.15;margin-top:4px}
.newsletter{position:absolute;left:88px;top:2528px;width:1021px;height:142px;background:var(--white);border-radius:30px;box-shadow:0 8px 30px rgba(224,71,154,.12)}

/* work */
.work-img{position:absolute;top:2878px;width:215px;height:216px;border-radius:0 0 34px 0}
.arrow-btn{position:absolute;top:2980px;width:26px;height:26px;border:1.5px solid var(--pink);border-radius:50%}

/* contact */
.contact-card{position:absolute;left:91px;top:3189px;width:622px;height:544px;background:var(--white);border-radius:0 0 90px 0;box-shadow:0 6px 24px rgba(0,0,0,.12)}
.field{position:absolute;font-size:16px;color:#333}
.field .line{position:absolute;left:0;height:1px;background:#999}

/* footer */
.footer{top:3797px;height:263px;background:var(--night);color:var(--white)}
.brand-foot{left:0;width:1200px;justify-content:center;top:36px;font-size:26px}
.brand-foot .dot{width:38px;height:38px}
.footer .links a{position:absolute;top:187px;font-size:17px;font-weight:600;color:var(--white);text-decoration:none}
.social{position:absolute;top:134px;width:26px;height:26px;border-radius:50%;background:var(--white)}
</style>
</head>
<body>

<!-- HERO -->
<section class="band hero">
  <svg class="abs" style="left:0;top:0" width="1200" height="577">
    <circle cx="370" cy="240" r="310" fill="#f9dcea" opacity=".7"/>
    <circle cx="930" cy="255" r="332" fill="var(--pink)"/>
  </svg>
  <div class="photo" role="img" aria-label="Team of colleagues gathered around a laptop in an office" style="left:628px;top:-60px;width:604px;height:620px;border-radius:50%;background:linear-gradient(135deg,#5b6670,#2c3238 55%,#8a7a6c)"></div>
  <div class="brand brand-head"><span class="dot"></span>Lumenway PR</div>
  <nav class="nav">
    <a class="active" style="left:259px">Home</a>
    <a style="left:334px">About</a>
    <a style="left:410px">Expertise</a>
    <a style="left:511px">News</a>
    <a style="left:582px">Work</a>
  </nav>
  <a class="contact-btn">CONTACT</a>
  <h1 class="abs" style="left:91px;top:175px;font-size:57px">WE ARE BUILDING<br>RELATIONSHIPS</h1>
  <p class="abs copy" style="left:91px;top:331px">Thinking beyond media relations and marketing<br>services, we understand the needs of our clients,<br>and our experts and our creative staff are working on<br>building long-term relationships. Anywhere in the world.</p>
  <div class="btn" style="left:91px;top:432px;width:169px;height:38px">EXPLORE</div>
</section>

<!-- WHO WE ARE -->
<section class="band" style="top:577px;height:756px">
  <svg class="abs" style="left:0;top:0" width="1200" height="756">
    <circle cx="1010" cy="320" r="420" fill="var(--blush-soft)"/>
    <circle cx="962" cy="353" r="378" fill="var(--blush)"/>
  </svg>
  <div class="photo" role="img" aria-label="Colleagues reviewing work on a laptop" style="left:88px;top:90px;width:257px;height:260px;background:linear-gradient(135deg,#b9c3cc,#5d6b78)"></div>
  <div class="photo" role="img" aria-label="Smiling woman in an orange sweater holding a tablet" style="left:367px;top:211px;width:257px;height:272px;border-radius:0 0 34px 0;background:linear-gradient(135deg,#6b5a48,#e2832e)"></div>
  <div class="photo" role="img" aria-label="Business team meeting around a table" style="left:88px;top:388px;width:257px;height:279px;border-radius:0 0 34px 0;background:linear-gradient(135deg,#d8d4cc,#7b6e62)"></div>
  <div class="kicker abs" style="left:667px;top:228px">WHO ARE WE? <span>→</span></div>
  <h2 class="abs" style="left:667px;top:275px;font-size:44px">WE ARE CREATING<br>UNIQUE VALUES.</h2>
  <p class="abs copy" style="left:667px;top:398px">Thinking beyond media relations and marketing<br>services, we understand the needs of our clients,<br>and our experts and our creative staff are working on<br>building long-term relationships. Anywhere in the world.</p>
  <div class="btn" style="left:667px;top:492px;width:169px;height:38px">LEARN MORE</div>
</section>

<!-- EXPERTISE -->
<section class="band expertise">
  <div class="kicker abs" style="left:88px;top:170px">OUR EXPERTISE <span>→</span></div>
  <h2 class="abs" style="left:88px;top:215px;font-size:44px">PRACTICES</h2>
  <p class="abs copy" style="left:93px;top:288px">To make choosing much easier for You,<br>we provide the widest possible range of services.<br>Let it be media relations, crisis management or<br>marketing services, our experts are always available.</p>
  <div class="btn" style="left:91px;top:383px;width:169px;height:38px">SEE ALL</div>
</section>
<div class="card" style="left:542px;top:1408px">
  <svg viewBox="0 0 52 52"><circle cx="26" cy="26" r="20"/><path d="M6 26h40M26 6v40M12 14c8 5 20 5 28 0M12 38c8-5 20-5 28 0"/></svg>
  <h3>B2B MARKETING</h3><p>The communication with business partners may be the...</p><div class="more">READ MORE</div>
</div>
<div class="card" style="left:840px;top:1437px">
  <svg viewBox="0 0 52 52"><rect x="6" y="8" width="14" height="14" rx="2"/><rect x="32" y="8" width="14" height="14" rx="2"/><rect x="6" y="32" width="14" height="14" rx="2"/><circle cx="39" cy="39" r="7"/><path d="M20 15h12M13 22v10M20 39h12"/></svg>
  <h3>SOCIAL MEDIA</h3><p>Using social media is one of the largest challenge...</p><div class="more">READ MORE</div>
</div>
<div class="card" style="left:542px;top:1651px">
  <svg viewBox="0 0 52 52"><circle cx="26" cy="20" r="12"/><circle cx="26" cy="20" r="6"/><path d="M18 30l-5 16 7-4 4 6 2-12M34 30l5 16-7-4-4 6-2-12"/></svg>
  <h3>BRAND MARKETING</h3><p>Recently, the significance of ideas have become much larger. It ...</p><div class="more">READ MORE</div>
</div>
<div class="card" style="left:840px;top:1676px">
  <svg viewBox="0 0 52 52"><circle cx="26" cy="26" r="18"/><ellipse cx="26" cy="20" rx="8" ry="3"/><path d="M18 20v12c0 2 4 3 8 3s8-1 8-3V20M18 26c0 2 4 3 8 3s8-1 8-3"/></svg>
  <h3>DATA &amp; ANALYTICS</h3><p>Knowledge is power. We hear this sentence often...</p><div class="more">READ MORE</div>
</div>

<!-- NEWS -->
<section class="band" style="top:1940px;height:858px">
  <svg class="abs" style="left:0;top:0" width="1200" height="858">
    <circle cx="1000" cy="300" r="420" fill="var(--blush-soft)"/>
    <circle cx="150" cy="560" r="270" fill="var(--blush-soft)"/>
  </svg>
  <div class="abs" style="left:0;width:1200px;top:90px;text-align:center;font-size:26px;font-weight:500">NEWS</div>
  <h2 class="abs" style="left:0;width:1200px;top:136px;text-align:center;font-size:44px">LATEST UPDATES</h2>
  <svg class="abs" style="left:580px;top:520px" width="40" height="12"><circle cx="6" cy="6" r="3.5" fill="#f2b8d5"/><circle cx="19" cy="6" r="3.5" fill="var(--pink)"/><circle cx="32" cy="6" r="3.5" fill="#f2b8d5"/></svg>
</section>
<div class="news-card" style="left:145px"><div class="photo" role="img" aria-label="Video editing workstation showing a news presenter" style="inset:0;background:linear-gradient(135deg,#2b4b6a,#6c6f74)"></div><div class="shade"></div><div class="txt"><b>Lorem Ipsum</b><p>Lorem Ipsum, giving information on its origins, as well as a random Lipsum generator.</p></div></div>
<div class="news-card" style="left:471px"><div class="photo" role="img" aria-label="Woman working at a desk with code on monitors" style="inset:0;background:linear-gradient(135deg,#3a3330,#8a6f5c)"></div><div class="shade"></div><div class="txt"><b>Lorem Ipsum</b><p>Lorem Ipsum, giving information on its origins, as well as a random Lipsum generator.</p></div></div>
<div class="news-card" style="left:793px"><div class="photo" role="img" aria-label="Colleagues reviewing charts together" style="inset:0;background:linear-gradient(135deg,#4a4646,#b7a8a2)"></div><div class="shade"></div><div class="txt"><b>Lorem Ipsum</b><p>Lorem Ipsum, giving information on its origins, as well as a random Lipsum generator.</p></div></div>

<div class="newsletter">
  <div class="abs" style="left:78px;top:44px;font-size:21px;font-weight:700">NEWSLETTER</div>
  <div class="abs" style="left:78px;top:83px;font-size:16px;color:#333">Want to grow your business? Subscribe our newsletter</div>
  <div class="btn" style="left:774px;top:52px;width:169px;height:37px">SUBSCRIBE</div>
</div>

<!-- WORK -->
<div class="kicker abs" style="left:88px;top:2782px">OUR WORK <span>→</span></div>
<div class="arrow-btn" style="left:91px"><svg width="23" height="23" viewBox="0 0 23 23"><path d="M13 7l-4 4.5 4 4.5" fill="none" stroke="var(--pink)" stroke-width="1.5"/></svg></div>
<div class="arrow-btn" style="left:1081px"><svg width="23" height="23" viewBox="0 0 23 23"><path d="M10 7l4 4.5-4 4.5" fill="none" stroke="var(--pink)" stroke-width="1.5"/></svg></div>
<div class="work-img" role="img" aria-label="Presenter showing a tablet to a team" style="left:143px;background:linear-gradient(135deg,#2d3440,#6b6f78)"></div>
<div class="work-img" role="img" aria-label="Hands typing on a laptop with a calendar app" style="left:377px;background:linear-gradient(135deg,#e6e4e2,#a9a6a4)"></div>
<div class="work-img" role="img" aria-label="Person browsing a phone at a desk with a lamp" style="left:609px;background:linear-gradient(135deg,#4a3a33,#b89d84)"></div>
<div class="work-img" role="img" aria-label="Laptop showing a marketing dashboard" style="left:841px;background:linear-gradient(135deg,#d9d4cf,#6c6a6a)"></div>

<!-- CONTACT -->
<svg class="abs" style="left:0;top:3100px" width="1200" height="700">
  <circle cx="1040" cy="300" r="270" fill="var(--blush-soft)"/>
  <circle cx="1009" cy="354" r="236" fill="var(--blush)"/>
  <circle cx="140" cy="560" r="230" fill="var(--blush-soft)"/>
</svg>
<div class="photo" role="img" aria-label="Smiling businessman in a navy suit with arms crossed" style="left:713px;top:3249px;width:396px;height:551px;border-radius:190px 190px 0 0;background:linear-gradient(180deg,#c9a58c 0%,#24386a 38%,#1b2a55)"></div>
<div class="contact-card">
  <h2 class="abs" style="left:59px;top:50px;font-size:44px;font-weight:700">Contact Us</h2>
  <div class="field" style="left:59px;top:154px">Name:<span class="line" style="top:38px;width:236px"></span></div>
  <div class="field" style="left:325px;top:154px">EMAIL:<span class="line" style="top:38px;width:232px"></span></div>
  <div class="field" style="left:59px;top:294px">NUMBER:<span class="line" style="top:38px;width:236px"></span></div>
  <div class="field" style="left:325px;top:294px">COUNTRY:<span class="line" style="top:38px;width:232px"></span></div>
  <div class="field" style="left:59px;top:438px">MESSAGE<span class="line" style="top:42px;width:429px"></span></div>
  <svg class="abs" style="left:501px;top:428px" width="62" height="62"><circle cx="31" cy="31" r="31" fill="var(--pink)"/><path d="M18 24l28-6-10 28-6-12z M30 34l16-16" fill="none" stroke="#fff" stroke-width="2" stroke-linejoin="round"/></svg>
</div>

<!-- FOOTER -->
<footer class="band footer">
  <svg class="abs" style="left:0;top:0" width="1200" height="263">
    <path d="M0 0h120C40 10 0 60 0 120z" fill="var(--white)"/>
    <circle cx="1090" cy="250" r="200" fill="#3a3a3c"/>
    <circle cx="40" cy="330" r="170" fill="#2a2a2c"/>
  </svg>
  <div class="brand brand-foot"><span class="dot"></span>Lumenway PR</div>
  <span class="social" style="left:506px"></span>
  <span class="social" style="left:561px"></span>
  <span class="social" style="left:613px"></span>
  <span class="social" style="left:667px"></span>
  <nav class="links">
    <a style="left:381px">Home</a>
    <a style="left:475px">About</a>
    <a style="left:568px">Expertise</a>
    <a style="left:687px">News</a>
    <a style="left:776px">Work</a>
  </nav>
  <div class="abs" style="left:88px;top:221px;width:1021px;height:1px;background:#444"></div>
  <div class="abs" style="left:0;width:1200px;top:238px;text-align:center;font-size:15px;font-weight:600">COPYRIGHT©2023 LUMENWAY PR. All Rights Reserved</div>
</footer>

</body>
</html>
```